Audio-Visual & Video Communications Business Requires a Cutting-edge Business Card Design

LinkVessel is a new Audio-Visual & Video Communications company in Cape Town, South Africa that is looking for a cutting-edge business card design. We sell these products to the Corporate, Education & Hospitality markets and will also host an Online Shop for companies and individuals to purchase our products online.

We are already using the following two colours in our logo and draft website. Please incorporate these colours into the design. Please note that our website is still in the design stage if you need to visit it. Green #a0ce4e & Dark Grey #333333.
Updates

Hi,

Please note that I have uploaded our logo in an .eps format.

Target Market(s)

Corporate Companies, Education Institutions & Hospitality Markets

Industry/Entity Type

Business

Requirements
Nice to have
• It would be great if you could incorporate the services that we offer.

1. Consultation & Design
2. Project Management
3. Supply & Installation
4. Onsite Support Personal
5. Online Shop

```html
<!DOCTYPE html>
<html lang="en">
<head>
<meta charset="utf-8">
<title>LinkVessel Business Card</title>
<link rel="stylesheet" href="https://fonts.googleapis.com/css2?family=Source+Sans+3:wght@400;600;700&display=swap">
<style>
  :root {
    --green: #a0ce4e;
    --grey-dark: #333333;
    --grey-type: #58595b;
    --grey-band: #5e5f61;
    --grey-soft: #6d6e70;
    --white: #ffffff;
    --backdrop: #e6e6e6;
  }
  * { box-sizing: border-box; margin: 0; padding: 0; }
  html, body {
    width: 1200px; height: 900px; overflow: hidden;
    background: var(--backdrop);
    font-family: "Source Sans 3", "Myriad Pro", sans-serif;
  }
  .canvas { position: relative; width: 1200px; height: 900px; }
  .card {
    position: absolute; top: 308px;
    width: 514px; height: 284px;
    background: var(--white);
    box-shadow: 0 2px 6px rgba(0,0,0,.18);
    overflow: hidden;
  }
  .card--front { left: 72px; }
  .card--back { left: 614px; }

  /* front */
  .front__mark {
    position: absolute; left: 50%; top: 78px;
    width: 54px; height: 54px; margin-left: -27px;
    border-radius: 50%; background: var(--green);
  }
  .front__name {
    position: absolute; left: 0; right: 0; top: 176px;
    text-align: center; font-weight: 700; font-size: 40px;
    letter-spacing: -0.5px; color: var(--grey-type); line-height: 1;
  }
  .front__web {
    position: absolute; left: 0; right: 0; top: 250px;
    text-align: center; font-size: 13px; letter-spacing: 3.6px;
    color: var(--grey-soft);
  }

  /* back */
  .back__band {
    position: absolute; left: 0; top: 0; width: 100%; height: 158px;
    background: var(--grey-band);
  }
  .back__mark {
    position: absolute; left: 110px; top: 30px;
    width: 54px; height: 54px; border-radius: 50%;
    background: var(--green);
  }
  .back__name {
    position: absolute; left: 42px; top: 112px;
    font-weight: 700; font-size: 29px; color: var(--white);
    line-height: 1; letter-spacing: -0.3px;
  }
  .services {
    position: absolute; left: 306px; top: 40px; list-style: none;
    color: var(--white); font-size: 14px; line-height: 17.5px;
  }
  .services li { padding-left: 14px; position: relative; }
  .services li::before {
    content: ""; position: absolute; left: 0; top: 6px;
    width: 6px; height: 6px; background: var(--white);
  }
  .person { position: absolute; left: 43px; top: 190px; color: var(--grey-type); }
  .person__name { font-weight: 700; font-size: 21px; line-height: 1.1; }
  .person__role { font-weight: 700; font-size: 15px; margin-top: 2px; }
  .person__mail { font-size: 14px; margin-top: 1px; display: flex; align-items: center; gap: 5px; }
  .contact {
    position: absolute; left: 302px; top: 180px; color: var(--grey-type);
    font-size: 13.5px; line-height: 17.5px; list-style: none;
  }
  .contact li { display: flex; gap: 5px; }
  .contact .icon { width: 12px; flex: none; padding-top: 3px; }
  .icon svg { display: block; fill: var(--grey-type); }
</style>
</head>
<body>
<main class="canvas">
  <section class="card card--front">
    <div class="front__mark"></div>
    <div class="front__name">LinkVessel</div>
    <div class="front__web">www.linkvessel.com</div>
  </section>

  <section class="card card--back">
    <div class="back__band">
      <div class="back__mark"></div>
      <div class="back__name">LinkVessel</div>
      <ul class="services">
        <li>Consultation &amp; Design</li>
        <li>Project Management</li>
        <li>Supply &amp; Installation</li>
        <li>Onsite Support Personal</li>
        <li>Online Shop</li>
      </ul>
    </div>

    <div class="person">
      <div class="person__name">Daniel Marlow</div>
      <div class="person__role">managing director</div>
      <div class="person__mail">
        <span class="icon"><svg width="11" height="8" viewBox="0 0 11 8"><rect width="11" height="8"/><path d="M0 0l5.5 4.5L11 0" fill="none" stroke="#fff" stroke-width="1"/></svg></span>
        info@lkv.com
      </div>
    </div>

    <ul class="contact">
      <li>
        <span class="icon"><svg width="10" height="13" viewBox="0 0 10 13"><path d="M5 0a5 5 0 0 0-5 5c0 3.5 5 8 5 8s5-4.5 5-8a5 5 0 0 0-5-5zm0 7a2 2 0 1 1 0-4 2 2 0 0 1 0 4z"/></svg></span>
        <span>45 Harbour Road<br>Sea Point, Cape Town 8005<br>Office 68</span>
      </li>
      <li>
        <span class="icon"><svg width="11" height="11" viewBox="0 0 11 11"><path d="M2.2 0L4 2.6 2.9 3.9c.8 1.7 2.5 3.4 4.2 4.2L8.4 7 11 8.8 9.7 11C4.5 10.7.3 6.5 0 1.3z"/></svg></span>
        <span>021 448 20 16</span>
      </li>
      <li>
        <span class="icon"><svg width="12" height="11" viewBox="0 0 12 11"><rect x="3" y="0" width="6" height="3"/><rect x="0" y="3.5" width="12" height="5" rx="1"/><rect x="3" y="7" width="6" height="4"/></svg></span>
        <span>021 448 20 17</span>
      </li>
    </ul>
  </section>
</main>
</body>
</html>
```